Four in One (Flexible infographic for Content Management Industry)

See attachment.
A graphic depicting 4 products, where each can stand on its own and each can be combined with others, but where, if all are taken together, the best result is achieved (the "super product").
Intended use is web. See attached file as an example.
The most basic idea is as the attached diagram shows, where 4 rectangles are arranged in a quadrangle, with a middle rectangle in the center representing the combined 4 products. This concept is fine except it is a bit too obvious as it stands. We are looking for either a variation of this or another concept.
The audience is technical + professional + enterprise - NOT consumers. Hence the design should be conservative in nature.
We are aware of tools like as Canva or Pictogram where such graphics are available, but we are looking for something with a bit more imagination and flexibility.
This graphic should be targeted to web sites and be delivered with vector-based (SVG) graphics.

```html
<!DOCTYPE html>
<html lang="en">
<head>
<meta charset="utf-8">
<title>Super Product – Four in One</title>
<link rel="stylesheet" href="https://fonts.googleapis.com/css2?family=Poppins:wght@400;700&display=swap">
<style>
  :root {
    --bg: #ffffff;
    --ink: #444444;
    --body-ink: #4a4a4a;
    --connector: #86e3f7;
    --hub-glow: rgba(110, 220, 250, 0.55);
    --docs: #55b0c8;
    --docs-glow: rgba(85, 176, 200, 0.5);
    --security: #57bb45;
    --security-glow: rgba(87, 187, 69, 0.45);
    --erp: #e06e12;
    --erp-glow: rgba(224, 110, 18, 0.45);
    --digital: #3585d3;
    --digital-glow: rgba(53, 133, 211, 0.45);
  }
  * { margin: 0; padding: 0; box-sizing: border-box; }
  html, body {
    width: 1200px; height: 1200px; overflow: hidden;
    background: var(--bg);
    font-family: "Poppins", sans-serif;
  }
  .canvas { position: relative; width: 1200px; height: 1200px; overflow: hidden; }
  .connectors { position: absolute; inset: 0; }
  .hub {
    position: absolute; left: 15px; top: 538px; width: 246px; height: 110px;
    background: #fff; border-radius: 26px;
    box-shadow: 0 0 14px 4px var(--hub-glow);
    display: flex; align-items: center; padding-left: 15px;
  }
  .hub-title { font-weight: 700; font-size: 30px; color: var(--ink); letter-spacing: -0.2px; }
  .product {
    position: absolute; width: 370px; height: 370px;
    background: #fff; border-radius: 58px;
  }
  .product-label {
    position: absolute; height: 33px; width: 320px; border-radius: 4px;
    color: #fff; font-weight: 700; font-size: 21px; line-height: 33px;
    white-space: nowrap; overflow: hidden;
  }
  .product-text {
    position: absolute; width: 310px;
    font-size: 17px; line-height: 19.8px; color: var(--body-ink); font-weight: 400;
  }
  .product-text p + p { margin-top: 19.8px; }

  .product--docs { left: 362px; top: 203px; box-shadow: 0 0 14px 3px var(--docs-glow); }
  .product--docs .product-label { left: 27px; top: 24px; background: var(--docs); padding-left: 13px; }
  .product--docs .product-text { left: 39px; top: 111px; }

  .product--security { left: 362px; top: 615px; box-shadow: 0 0 14px 3px var(--security-glow); }
  .product--security .product-label { left: 27px; top: 34px; background: var(--security); padding-left: 9px; }
  .product--security .product-text { left: 39px; top: 147px; }

  .product--erp { left: 768px; top: 17px; box-shadow: 0 0 14px 3px var(--erp-glow); }
  .product--erp .product-label { left: 24px; top: 28px; background: var(--erp); padding-left: 0; }
  .product--erp .product-text { left: 53px; top: 105px; }

  .product--digital { left: 768px; top: 815px; box-shadow: 0 0 14px 3px var(--digital-glow); }
  .product--digital .product-label { left: 42px; top: 29px; background: var(--digital); padding-left: 20px; }
  .product--digital .product-text { left: 53px; top: 131px; }
</style>
</head>
<body>
<main class="canvas">
  <svg class="connectors" width="1200" height="1200" viewBox="0 0 1200 1200" aria-hidden="true">
    <g fill="none" stroke="var(--connector)" stroke-width="11" stroke-linecap="butt">
      <path d="M261 591 H301"/>
      <path d="M801 137 H341 Q301 137 301 177 V970 Q301 1010 341 1010 L780 1003"/>
      <path d="M368 371 H341 Q301 371 301 411"/>
      <path d="M301 770 Q301 810 341 810 H368"/>
    </g>
  </svg>

  <div class="hub"><h1 class="hub-title">Super Product</h1></div>

  <section class="product product--docs">
    <h2 class="product-label">Document Management</h2>
    <div class="product-text">
      <p>A graphic depicting 4 products, where each can stand on its own and each can be combined with others, but where, if all are taken together, the best result is achieved (the "super product").</p>
      <p>Intended use is web. See attached</p>
    </div>
  </section>

  <section class="product product--security">
    <h2 class="product-label">Secrity and Compliance</h2>
    <div class="product-text">
      <p>A graphic depicting 4 products, where each can stand on its own and each can be combined with others, but where, if all are taken together, the best result is achieved (the "super product").</p>
      <p>Intended use is web. See attached</p>
    </div>
  </section>

  <section class="product product--erp">
    <h2 class="product-label">Enterprise Resource Planning</h2>
    <div class="product-text">
      <p>A graphic depicting 4 products, where each can stand on its own and each can be combined with others, but where, if all are taken together, the best result is achieved (the "super product").</p>
      <p>Intended use is web. See attached</p>
    </div>
  </section>

  <section class="product product--digital">
    <h2 class="product-label">Digital Transformation</h2>
    <div class="product-text">
      <p>A graphic depicting 4 products, where each can stand on its own and each can be combined with others, but where, if all are taken together, the best result is achieved (the "super product").</p>
      <p>Intended use is web. See attached</p>
    </div>
  </section>
</main>
</body>
</html>
```